For Lease sign for Property management company in Kansas City

We need someone to take our information and design a standard for lease sign that we can put in front of each of our buildings. I would love for it to do its job of letting people know there are units available but also be unique somehow. Also the aspect ratio of the design would ideally be 4 wide by 3 tall but we open to other ideas. It will be a larger yard sign.

Target Market(s)

Potential Tenants

Industry/Entity Type

Real Estate Development

Font styles to use
Sans Serif

Requirements
Must have
• Our logo, our website (www.tollen-estates.com), our phone number (816) 247-5903.
Nice to have
• Some how say "For Lease"
Sign to be 4' wide by 3' tall
If there was a place to put the building name that would be cool but not ne
Should not have
• Nothing that I can think of

```html
<!DOCTYPE html>
<html lang="en">
<head>
<meta charset="utf-8">
<title>Tollen Estates – For Lease Yard Sign</title>
<link rel="stylesheet" href="https://fonts.googleapis.com/css2?family=Montserrat:wght@500;600&family=Oswald:wght@600&display=swap">
<style>
  :root {
    --sign-red: #bc0a26;
    --sign-red-deep: #a10820;
    --sign-gold: #f7b036;
    --sign-gold-edge: #e09a2a;
    --paper: #ffffff;
  }
  html, body {
    margin: 0;
    padding: 0;
    width: 1008px;
    height: 1200px;
    overflow: hidden;
    background: var(--paper);
  }
  .canvas {
    position: relative;
    width: 1008px;
    height: 1200px;
  }
  .yard-sign {
    position: absolute;
    left: 0;
    top: 0;
    width: 1008px;
    height: 1200px;
  }
  .brand-name {
    font-family: "Montserrat", sans-serif;
    font-weight: 600;
    fill: var(--paper);
  }
  .headline {
    font-family: "Oswald", sans-serif;
    font-weight: 600;
    fill: var(--paper);
  }
  .building-label {
    font-family: "Montserrat", sans-serif;
    font-weight: 600;
    fill: var(--sign-red);
  }
  .website {
    font-family: "Montserrat", sans-serif;
    font-weight: 600;
    fill: var(--sign-red);
  }
  .phone {
    font-family: "Oswald", sans-serif;
    font-weight: 600;
    fill: var(--sign-red);
  }
</style>
</head>
<body>
<main class="canvas">
  <svg class="yard-sign" viewBox="0 0 1008 1200" xmlns="http://www.w3.org/2000/svg" aria-label="Tollen Estates For Lease yard sign">
    <!-- outer frame -->
    <rect class="sign-frame" x="147" y="129" width="714" height="533" fill="var(--paper)" stroke="var(--sign-red)" stroke-width="6"/>

    <!-- red field with wave bottom -->
    <path class="sign-field" d="M158 139 H850 V578 C790 566 730 556 660 560 C560 565 450 585 330 590 C260 592 205 583 158 568 Z" fill="var(--sign-red)"/>

    <!-- long shadow under building tag -->
    <path class="tag-shadow" d="M345 535 L668 535 L679 560 C600 564 520 574 445 581 L372 581 Z" fill="var(--sign-red-deep)"/>

    <!-- brand -->
    <circle class="brand-dot" cx="292" cy="251" r="85" fill="var(--sign-gold)"/>
    <text class="brand-name" x="408" y="262" font-size="96" textLength="392" lengthAdjust="spacingAndGlyphs">TOLLEN</text>
    <text class="brand-name" x="408" y="315" font-size="56" textLength="392" lengthAdjust="spacing">ESTATES</text>

    <!-- headline -->
    <text class="headline" x="281" y="481" font-size="168" textLength="450" lengthAdjust="spacingAndGlyphs">FOR LEASE</text>

    <!-- building name tag -->
    <rect class="building-tag" x="336" y="498" width="336" height="49" rx="24.5" fill="var(--sign-gold)" stroke="var(--sign-gold-edge)" stroke-width="2"/>
    <text class="building-label" x="504" y="532" font-size="27" text-anchor="middle">BUILDING NAME</text>

    <!-- contact -->
    <text class="website" x="198" y="632" font-size="19.5" textLength="286" lengthAdjust="spacingAndGlyphs">www.tollen-estates.com</text>
    <text class="phone" x="548" y="636" font-size="64" textLength="256" lengthAdjust="spacingAndGlyphs">(816) 247-5903</text>
  </svg>
</main>
</body>
</html>
```